LLC needs a business card design that emphasizes consulting and expert witness in upstream oil and g

I need a business card design for my company called Velmo Consultative Service, LLC. My expertise is in oil and gas upstream operations management to optimize performance and also as an expert witness for law firms in oil and gas upstream operations litigation.
The final design should communicate knowledge and hands-on experience as well as trust. (Velmo means rope or lasso. Perhaps "Velmo" should be in the form of a rope.) I do not like the color green in any shade. My first preference would be some shade of blue.

```html
<!DOCTYPE html>
<html lang="en">
<head>
<meta charset="UTF-8">
<title>Velmo Consultative Service — Business Cards</title>
<link href="https://fonts.googleapis.com/css2?family=Tinos:wght@400;700&display=swap" rel="stylesheet">
<style>
  :root {
    --stage: #eceef1;
    --navy-deep: #12305f;
    --navy: #1d4785;
    --blue-mid: #3f6fb3;
    --blue-light: #8fb0de;
    --brand-blue: #1f4f9c;
    --ink-grey: #6c6f75;
    --paper: #ffffff;
    --faint: #ececec;
    --white: #ffffff;
  }
  * { box-sizing: border-box; margin: 0; padding: 0; }
  html, body {
    width: 1200px; height: 784px; overflow: hidden;
    background: var(--stage);
    font-family: "Tinos", "Times New Roman", serif;
  }
  .canvas {
    position: relative; width: 1200px; height: 784px;
  }
  .card {
    position: absolute; width: 540px; height: 308px;
    border-radius: 4px; overflow: hidden;
    box-shadow: 0 6px 18px rgba(20, 30, 50, 0.18);
  }
  .card--front { left: 40px; top: 238px; background: var(--navy-deep); }
  .card--back  { left: 620px; top: 238px; background: var(--paper); }

  .front-pattern {
    position: absolute; inset: 0;
    background:
      radial-gradient(ellipse at 80% 30%, var(--blue-light) 0%, var(--blue-mid) 35%, transparent 70%),
      linear-gradient(120deg, var(--navy-deep) 0%, var(--navy) 45%, var(--blue-mid) 100%);
  }

  .wordmark {
    position: absolute; display: flex; align-items: center; gap: 14px;
  }
  .wordmark__dot { width: 58px; height: 58px; border-radius: 50%; flex: none; }
  .wordmark__text { display: flex; flex-direction: column; line-height: 1; }
  .wordmark__name { font-size: 56px; font-weight: 700; }
  .wordmark__tag { font-size: 19px; font-weight: 400; margin-top: 4px; letter-spacing: 0.3px; }

  .card--front .wordmark { left: 120px; top: 92px; }
  .card--front .wordmark__dot { background: var(--white); }
  .card--front .wordmark__name,
  .card--front .wordmark__tag { color: var(--white); }

  .card--back .wordmark { left: 48px; top: 58px; }
  .card--back .wordmark__dot { background: var(--brand-blue); }
  .card--back .wordmark__name { color: var(--brand-blue); }
  .card--back .wordmark__tag { color: var(--ink-grey); }

  .back-accent {
    position: absolute; right: -40px; top: 30px;
    width: 220px; height: 220px; border-radius: 50%;
    background: var(--faint);
  }

  .contact {
    position: absolute; left: 48px; top: 178px;
    list-style: none; color: var(--ink-grey); font-size: 16px; line-height: 1.3;
  }
  .contact__item { display: flex; align-items: flex-start; gap: 8px; }
  .contact__icon { width: 16px; height: 16px; flex: none; margin-top: 2px; }
  .contact__icon * { fill: var(--brand-blue); }
  .contact__indent { padding-left: 24px; }
</style>
</head>
<body>
<main class="canvas">

  <section class="card card--front" aria-label="Card front">
    <div class="front-pattern" role="img" aria-label="Blue background with a sweeping pattern of pale blue dots"></div>
    <div class="wordmark">
      <span class="wordmark__dot"></span>
      <div class="wordmark__text">
        <span class="wordmark__name">Velmo</span>
        <span class="wordmark__tag">Consultative Service</span>
      </div>
    </div>
  </section>

  <section class="card card--back" aria-label="Card back">
    <div class="back-accent" aria-hidden="true"></div>
    <div class="wordmark">
      <span class="wordmark__dot"></span>
      <div class="wordmark__text">
        <span class="wordmark__name">Velmo</span>
        <span class="wordmark__tag">Consultative Service</span>
      </div>
    </div>

    <ul class="contact">
      <li class="contact__item">
        <svg class="contact__icon" viewBox="0 0 16 16" aria-hidden="true"><path d="M3 1l3 3-1.6 1.8a9 9 0 0 0 5.8 5.8L12 10l3 3-2 2C6.5 15 1 9.5 1 3z"/></svg>
        <span>555-014-2290</span>
      </li>
      <li class="contact__item">
        <svg class="contact__icon" viewBox="0 0 16 16" aria-hidden="true"><path d="M1 3h14v10H1z M2.5 4.5L8 9l5.5-4.5v-0.3H2.5z" fill-rule="evenodd"/></svg>
        <span>info@velmoconsult.example</span>
      </li>
      <li class="contact__item">
        <svg class="contact__icon" viewBox="0 0 16 16" aria-hidden="true"><path d="M8 1a7 7 0 1 0 0 14A7 7 0 0 0 8 1zm0 1.5c.8 0 1.7 1.6 2 4.2H6c.3-2.6 1.2-4.2 2-4.2zM2.6 6.7A5.6 5.6 0 0 1 5.3 3a9 9 0 0 0-.9 3.7zm0 1.6h1.8c.1 1.5.4 2.8.9 3.7a5.6 5.6 0 0 1-2.7-3.7zm3.4 0h4c-.3 2.6-1.2 4.2-2 4.2s-1.7-1.6-2-4.2zm5.6 0h1.8a5.6 5.6 0 0 1-2.7 3.7c.5-.9.8-2.2.9-3.7zm0-1.6A9 9 0 0 0 10.7 3a5.6 5.6 0 0 1 2.7 3.7z"/></svg>
        <span>www.velmoconsult.example</span>
      </li>
      <li class="contact__item">
        <svg class="contact__icon" viewBox="0 0 16 16" aria-hidden="true"><path d="M8 1L0.5 8h2.2v7h4v-4.5h2.6V15h4V8h2.2z"/></svg>
        <span>4410 Harlow Ridge Road,</span>
      </li>
      <li class="contact__indent">Fort Kessel, Texas 79999</li>
    </ul>
  </section>

</main>
</body>
</html>
```